Business card design for Plumbing and Gas fitting company

We need a business card design for our plumbing and gas fitting company using the company logo and director details. Design should be modern and eye-catching however kept reasonably simple. This design should be targeted at commercial businesses/work so professionalism is key.

Target Market(s)

Commercial/business

Industry/Entity Type

Plumbing

Contact Information for Business Card

Warren Dohey
Director
027 581 9043
warren@vantorplumbingandgas.example
PO Box 7816
Palmerston North 4472

Font styles to use
Sans Serif

Requirements
Must have
• Logo
• Modern
• Kept simple
Nice to have
• Colour scheme based around logo

```html
<!DOCTYPE html>
<html lang="en">
<head>
<meta charset="utf-8">
<title>Vantor Plumbing &amp; Gas — Business Card</title>
<link href="https://fonts.googleapis.com/css2?family=Lato:wght@400;700;900&display=swap" rel="stylesheet">
<style>
  :root {
    --backdrop-light: #e4e4e4;
    --backdrop-dark: #a9a9a9;
    --brand-blue: #1567b5;
    --brand-blue-light: #1a8ccc;
    --brand-blue-deep: #0f5fb0;
    --card-white: #ffffff;
    --ink: #1e1e1e;
    --ink-soft: #333333;
    --edge-red: #c4373a;
  }
  * { box-sizing: border-box; margin: 0; padding: 0; }
  html, body {
    width: 1200px;
    height: 1000px;
    overflow: hidden;
  }
  body {
    background: radial-gradient(ellipse at 50% 40%, var(--backdrop-light) 0%, #cfcfcf 55%, var(--backdrop-dark) 100%);
    font-family: "Lato", sans-serif;
    position: relative;
  }
  .card {
    position: absolute;
    width: 560px;
    height: 320px;
    border-radius: 28px;
    box-shadow: 0 18px 30px rgba(0,0,0,0.28), 0 3px 6px rgba(0,0,0,0.18);
    overflow: hidden;
  }
  /* Front side */
  .card--front {
    left: 90px;
    top: 110px;
    background: radial-gradient(ellipse at 60% 75%, var(--brand-blue-light) 0%, var(--brand-blue) 55%, var(--brand-blue-deep) 100%);
    border-bottom: 2px solid var(--edge-red);
    display: flex;
    align-items: center;
    justify-content: center;
  }
  .brand-lockup {
    display: flex;
    align-items: center;
    gap: 16px;
  }
  .brand-dot {
    width: 34px;
    height: 34px;
    border-radius: 50%;
    flex: none;
  }
  .card--front .brand-dot { background: var(--card-white); }
  .brand-name {
    font-weight: 900;
    line-height: 1;
    white-space: nowrap;
  }
  .card--front .brand-name {
    color: var(--card-white);
    font-size: 38px;
  }
  /* Back side */
  .card--back {
    left: 560px;
    top: 540px;
    background: var(--card-white);
    display: flex;
    align-items: center;
    padding: 0 34px 0 34px;
  }
  .card--back .brand-lockup {
    width: 232px;
    gap: 10px;
    flex: none;
  }
  .card--back .brand-dot {
    width: 20px;
    height: 20px;
    background: var(--brand-blue);
  }
  .card--back .brand-name {
    color: var(--brand-blue);
    font-size: 18.5px;
  }
  .divider {
    width: 1.5px;
    height: 200px;
    background: var(--brand-blue);
    margin: 0 22px 0 8px;
    flex: none;
  }
  .contact {
    color: var(--ink-soft);
    font-size: 13px;
    line-height: 1.35;
  }
  .contact__name {
    font-size: 21px;
    font-weight: 700;
    color: var(--ink);
    line-height: 1.1;
  }
  .contact__role {
    font-size: 12px;
    font-weight: 700;
    color: var(--ink);
    margin: 2px 0 12px 18px;
  }
  .contact__block {
    margin-left: 18px;
    margin-bottom: 12px;
  }
  .contact__block:last-child { margin-bottom: 0; }
  .contact__line { display: block; white-space: nowrap; }
  .contact__indent { padding-left: 18px; }
</style>
</head>
<body>

  <section class="card card--front" aria-label="Business card front">
    <div class="brand-lockup">
      <span class="brand-dot" aria-hidden="true"></span>
      <span class="brand-name">Vantor Plumbing &amp; Gas</span>
    </div>
  </section>

  <section class="card card--back" aria-label="Business card back">
    <div class="brand-lockup">
      <span class="brand-dot" aria-hidden="true"></span>
      <span class="brand-name">Vantor Plumbing &amp; Gas</span>
    </div>
    <div class="divider" aria-hidden="true"></div>
    <div class="contact">
      <div class="contact__name">Warren Dohey</div>
      <div class="contact__role">Director</div>
      <div class="contact__block">
        <span class="contact__line">PO Box 7816</span>
        <span class="contact__line contact__indent">Palmerston North 4472</span>
      </div>
      <div class="contact__block">
        <span class="contact__line">027 581 9043</span>
      </div>
      <div class="contact__block">
        <span class="contact__line">warren@vantorplumbingandgas.example</span>
        <span class="contact__line">www.vantorplumbingandgas.example</span>
      </div>
    </div>
  </section>

</body>
</html>
```